Business Card Design

The business is a mobile physiotherapy, personal training and massage business located on the gold coast. I would like a design that works well with my logo that I had recently created by a graphic design company.

I have a mock business card made from the prinwell website. This may help with the design.

Target Market(s)

Any age although specifically for 30+

Industry/Entity Type

Graphic Design

Contact Information for Business Card

Summit Motion Physio
Mobile Physiotherapy, Personal Training & Massage Service
Location: Gold Coast
Marcus Tellwin
Dr. of Physiotherapy & B. Ex. Science
e: summitmotionphysio@mailbox.example
w: www.summitmotionphysio.example
m: 0455 726 309

```html
<!DOCTYPE html>
<html lang="en">
<head>
<meta charset="utf-8">
<title>Summit Motion Physio — Business Card</title>
<link href="https://fonts.googleapis.com/css2?family=Barlow+Condensed:wght@500;600;700&display=swap" rel="stylesheet">
<style>
  :root {
    --page: #ffffff;
    --card-black: #0b0b0b;
    --ring-dark: #2b2b2b;
    --ring-mid: #6a6a6a;
    --ring-light: #a9a9a9;
    --ring-core: #ffffff;
    --brand-red: #d10a0a;
    --text-light: #ffffff;
    --text-dark: #111111;
  }
  * { margin: 0; padding: 0; box-sizing: border-box; }
  html, body {
    width: 1200px; height: 1000px; overflow: hidden;
    background: var(--page);
    font-family: "Barlow Condensed", "Arial Narrow", sans-serif;
  }
  .sheet {
    position: relative; width: 1200px; height: 1000px;
    display: flex; align-items: center; justify-content: center; gap: 40px;
  }
  .card {
    position: relative; width: 540px; height: 328px;
    background: var(--card-black); overflow: hidden;
  }
  .brand {
    display: flex; align-items: center; gap: 8px;
    font-weight: 700; letter-spacing: 0.2px; line-height: 1; white-space: nowrap;
  }
  .brand-dot { width: 12px; height: 12px; border-radius: 50%; background: var(--brand-red); flex: none; }

  /* Front */
  .card-front .rings { position: absolute; inset: 0; }
  .card-front .brand {
    position: absolute; left: 50%; top: 50%; transform: translate(-50%, -50%);
    font-size: 30px; color: var(--text-dark);
  }

  /* Back */
  .card-back .red-band { position: absolute; inset: 0; }
  .card-back .brand {
    position: absolute; left: 30px; top: 44px;
    font-size: 30px; color: var(--text-light);
  }
  .tagline {
    position: absolute; left: 24px; top: 100px; width: 290px;
    color: var(--text-light); font-size: 11px; font-weight: 600;
    line-height: 1.35; text-align: center;
  }
  .athlete-art { position: absolute; left: 330px; top: 12px; width: 190px; height: 212px; }
  .contact {
    position: absolute; right: 14px; bottom: 14px;
    color: var(--text-light); font-size: 11.5px; font-weight: 500;
    line-height: 1.35; text-align: left; font-style: normal;
  }
</style>
</head>
<body>
<main class="sheet">

  <section class="card card-front" aria-label="Card front">
    <svg class="rings" viewBox="0 0 540 328" width="540" height="328" aria-hidden="true">
      <ellipse cx="270" cy="166" rx="236" ry="158" fill="var(--ring-dark)"/>
      <ellipse cx="270" cy="166" rx="196" ry="128" fill="var(--ring-mid)"/>
      <ellipse cx="270" cy="166" rx="160" ry="102" fill="var(--ring-light)"/>
      <ellipse cx="270" cy="166" rx="128" ry="80" fill="var(--ring-core)"/>
    </svg>
    <div class="brand"><span class="brand-dot"></span>Summit Motion Physio</div>
  </section>

  <section class="card card-back" aria-label="Card back">
    <svg class="red-band" viewBox="0 0 540 328" width="540" height="328" aria-hidden="true">
      <polygon points="0,328 540,120 540,328" fill="var(--brand-red)"/>
    </svg>
    <svg class="athlete-art" viewBox="0 0 190 212" width="190" height="212" role="img" aria-label="White silhouette of a running athlete inside a sweeping arc">
      <defs>
        <radialGradient id="athleteTone" cx="50%" cy="45%" r="60%">
          <stop offset="0%" stop-color="#ffffff"/>
          <stop offset="100%" stop-color="#cfcfcf"/>
        </radialGradient>
      </defs>
      <ellipse cx="95" cy="106" rx="90" ry="104" fill="url(#athleteTone)"/>
    </svg>

    <div class="brand"><span class="brand-dot"></span>Summit Motion Physio</div>
    <p class="tagline">Mobile Physiotherapy, Massage and Personal Training Service<br>Location: Gold Coast</p>

    <address class="contact">
      <div>Dr. of Physiotherapy &amp; B. Ex. Science</div>
      <div>Email: summitmotionphysio@mailbox.example</div>
      <div>Website: www.summitmotionphysio.example</div>
      <div>Mobile: 0455 726 309</div>
    </address>
  </section>

</main>
</body>
</html>
```